Healthcare IT company looking for business card design

We develop IT systems for healthcare that significantly reduces cost and improves quality.

We want a business card design that is professional and clean, and using the colors in our logo.

Target Market(s)

Doctors and decision makers in the healthcare industry

Industry/Entity Type

Healthcare

Contact Information for Business Card

It should include
Name and title, address, telephone

Tobias Vrenholt, CEO
+46 712 418257
tobias@kelvaro.se

Font styles to use
Serif

Colors
0355a3
ed282f

Requirements
Must have
• Clean design
• Professional feel
Nice to have
• N/A
Should not have
• N/A

```html
<!DOCTYPE html>
<html lang="en">
<head>
<meta charset="utf-8">
<title>Kelvaro – Business Card</title>
<link rel="stylesheet" href="https://fonts.googleapis.com/css2?family=Hind:wght@400;600;700&display=swap">
<style>
  :root {
    --brand-blue: #0355a3;
    --brand-red: #ed282f;
    --brand-red-deep: #b81c22;
    --paper: #ffffff;
    --backdrop: #e8e4dd;
    --ink-light: #ffffff;
  }
  * { margin: 0; padding: 0; box-sizing: border-box; }
  html, body {
    width: 1200px;
    height: 950px;
    overflow: hidden;
    background: var(--backdrop);
    font-family: "Hind", "Helvetica Neue", Arial, sans-serif;
  }
  .stage {
    width: 1200px;
    height: 950px;
    display: flex;
    flex-direction: column;
    align-items: center;
    justify-content: center;
    gap: 60px;
  }
  .card {
    position: relative;
    width: 640px;
    height: 366px;
    overflow: hidden;
    box-shadow: 0 6px 18px rgba(0, 0, 0, 0.18);
  }

  /* Back side */
  .card-back {
    background: linear-gradient(120deg, var(--brand-red) 0%, var(--brand-red) 55%, var(--brand-red-deep) 100%);
    display: flex;
    flex-direction: column;
    align-items: center;
    justify-content: center;
    color: var(--ink-light);
  }
  .card-back .brand-name {
    font-size: 64px;
    font-weight: 700;
    line-height: 1;
    letter-spacing: 1px;
  }
  .card-back .web {
    margin-top: 28px;
    font-size: 17px;
    font-weight: 400;
    letter-spacing: 4px;
  }

  /* Front side */
  .card-front { background: var(--paper); }
  .card-front .wave {
    position: absolute;
    inset: 0;
    width: 100%;
    height: 100%;
  }
  .card-front .wave .band { fill: var(--brand-blue); }
  .card-front .wave .stripe { fill: var(--brand-red); }
  .card-front .brand-name {
    position: absolute;
    left: 40px;
    top: 36px;
    font-size: 58px;
    font-weight: 700;
    line-height: 1;
    color: var(--brand-blue);
  }
  .contact {
    position: absolute;
    right: 30px;
    top: 194px;
    text-align: right;
    color: var(--ink-light);
    font-size: 14px;
    line-height: 1.35;
  }
  .contact .person-name {
    font-size: 21px;
    font-weight: 600;
    line-height: 1.1;
  }
  .contact .person-title {
    font-size: 14px;
    margin-bottom: 10px;
  }
  .contact .address { margin-bottom: 4px; }
  .contact .line {
    display: flex;
    justify-content: flex-end;
    align-items: center;
    gap: 7px;
  }
  .contact .icon {
    width: 14px;
    height: 14px;
    fill: var(--ink-light);
  }
</style>
</head>
<body>
<main class="stage">

  <section class="card card-back" aria-label="Business card back">
    <div class="brand-name">Kelvaro</div>
    <div class="web">kelvaro.se</div>
  </section>

  <section class="card card-front" aria-label="Business card front">
    <svg class="wave" viewBox="0 0 640 366" preserveAspectRatio="none" aria-hidden="true">
      <path class="stripe" d="M0,122 C100,172 170,204 260,198 C380,190 500,107 640,90 L640,98 C500,115 380,198 260,206 C170,212 100,180 0,132 Z"/>
      <path class="band" d="M0,140 C100,190 170,222 260,216 C380,208 500,125 640,108 L640,366 L0,366 Z"/>
    </svg>

    <div class="brand-name">Kelvaro</div>

    <div class="contact">
      <div class="person-name">Tobias Vrenholt</div>
      <div class="person-title">CEO</div>
      <div class="address">2716 Ashgrove Lane<br>Milford Park, NY 11090</div>
      <div class="line">
        <span>+46 712 418257</span>
        <svg class="icon" viewBox="0 0 16 16" aria-hidden="true"><path d="M3.5 1.5 L6 1.5 L7 5 L5.3 6.3 C6.2 8.2 7.8 9.8 9.7 10.7 L11 9 L14.5 10 L14.5 12.5 C14.5 13.6 13.6 14.5 12.5 14.5 C6.5 14.5 1.5 9.5 1.5 3.5 C1.5 2.4 2.4 1.5 3.5 1.5 Z"/></svg>
      </div>
      <div class="line">
        <span>tobias@kelvaro.se</span>
        <svg class="icon" viewBox="0 0 16 16" aria-hidden="true"><path d="M1 3.5 H15 V12.5 H1 Z M1.8 4.2 L8 9 L14.2 4.2 Z" fill-rule="evenodd"/></svg>
      </div>
      <div class="line">
        <span>www.kelvaro.se</span>
        <svg class="icon" viewBox="0 0 16 16" aria-hidden="true"><circle cx="8" cy="8" r="6.5"/><path d="M5 8 H11 M8 5 V11" stroke="#0355a3" stroke-width="1.4"/></svg>
      </div>
    </div>
  </section>

</main>
</body>
</html>
```